Marketplace Web Re-design overhaul @quarrynest

Hi,
We are currently in production with a website that is getting some mixed feedback about visual appeal and usability. We are using a responsive design and need to stay true to the logo colours and other marketing collateral we have in place. I will provide a brochure with the colour palate we use for some guidance. If you can please help us design something fresh and modern to communicate the essence of our company. The brochure will be a good summary of what we do and who we are targeting as customers. Our current website can be found at www.quarrynest.com. If there is any questions, please let me know.

Target Market(s)

Contractors and Corporate Companies

Industry/Entity Type

Information Technology

Number of Pages Required

4 page

Requirements
Must have
• Must have a complete new visual look, including
• 1. Images
• 2. Background colour scheme overhaul (not black)
• 3. re-design of the layout but keep to similar page breakdowns
Nice to have
• Some of the pages are a bit wordy, happy to have suggestions on how to reduce.
• Would be great if we can integrate the Plumb.ON! blog page to the Quarrynest page?
• This is some feedback a fellow UX designer provided to improve our CRO
• First off when you land on the home page, who is your audience? Are you everything to everyone? Even after watching the video (https://www.vidmarrow.net/watch?v=q7RtPe3LwZ0), I do not know what markets you service or who this app will be for.
• Your main headline and paragraph above the fold I find unnecessarily wordy and an overuse of 'buzzwords' . Perhaps you could look at appealing to the lowest common denominator and make it very simple and put it all into a simple sentence.
• The main hero image to the right of the headline offers no emotional pull at all. I'm assuming it's just a screenshot of your dashboard? Personally, I would be looking at using a person's image in that space.
• Also in this space, increase the size of your 'register' button. On the topic of your register button, you have it in different colours. Green in header, and red in content. Make it the same colour, and don't use that colour again on the site. That colour is to become your call to action (CTA) colour. Understandably you'll have three different colours for the account type, and again, don't use these colours anywhere else on the site.
• The registration area where the three account types are where you choose which one suits you, it's extremely busy with background images and heavy use of text. If you were my client, I would be advising you to ditch the bg image (including the Zelo shot), keeping the text, making the register icons much bigger. Perhaps instead of bg images, use a solid colour for each (green, orange, red). I'm highly confident this change will make a massive difference in your sign up rate.
Should not have
• Please keep to the fonts used on the original website
• Keep to the colour provided on the company brochure for guidance.

```html
<!DOCTYPE html>
<html lang="en">
<head>
<meta charset="utf-8">
<title>Quarrynest — Available, Quality Talent on Demand</title>
<link href="https://fonts.googleapis.com/css2?family=Roboto:wght@300;400;500;700&display=swap" rel="stylesheet">
<style>
  :root {
    --navy: #1a2233;
    --green: #37c057;
    --cta: #5cb85c;
    --orange: #f7902b;
    --red: #ee3a3a;
    --ink: #222a33;
    --muted: #666c73;
    --panel: #f4f4f4;
    --white: #ffffff;
  }
  * { box-sizing: border-box; margin: 0; padding: 0; }
  html, body { width: 1200px; height: 1200px; overflow: hidden; }
  body { font-family: "Roboto", Arial, sans-serif; color: var(--ink); background: var(--white); position: relative; }

  .site-header { position: absolute; top: 0; left: 0; width: 1200px; height: 62px; background: var(--navy); }
  .brand { position: absolute; left: 31px; top: 19px; display: flex; align-items: center; gap: 7px; color: #c9ced6; font-size: 16px; font-weight: 300; letter-spacing: 0.5px; }
  .brand-dot { width: 14px; height: 14px; border-radius: 50%; background: var(--green); }
  .main-nav a { position: absolute; top: 24px; color: var(--white); font-size: 11px; text-decoration: none; letter-spacing: 0.1px; }
  .btn-login { position: absolute; left: 759px; top: 15px; width: 93px; height: 32px; background: var(--white); color: var(--ink); font-size: 11px; display: flex; align-items: center; justify-content: center; letter-spacing: 0.4px; }
  .btn-register { position: absolute; left: 871px; top: 15px; width: 94px; height: 32px; background: var(--cta); color: var(--white); font-size: 11px; font-weight: 500; display: flex; align-items: center; justify-content: center; letter-spacing: 0.4px; }

  .hero { position: absolute; top: 62px; left: 0; width: 1200px; height: 525px;
    background: linear-gradient(100deg, #6f6a5e 0%, #8a8a80 35%, #9aa4ad 60%, #7f93aa 100%); }
  .hero-title { position: absolute; left: 234px; top: 198px; font-size: 32px; font-weight: 700; line-height: 38px; letter-spacing: -0.3px; }
  .hero-title .g { color: var(--green); }
  .hero-title .o { color: var(--orange); }
  .hero-title .r { color: var(--red); }
  .hero-copy { position: absolute; left: 234px; top: 281px; width: 430px; color: var(--white); font-size: 11.5px; line-height: 19px; }
  .join-outline { position: absolute; left: 242px; top: 359px; width: 124px; height: 31px; border: 1px solid var(--white); }
  .btn-join { position: absolute; left: 235px; top: 366px; width: 125px; height: 30px; background: var(--white); color: var(--ink); font-size: 10.5px; font-weight: 500; display: flex; align-items: center; justify-content: center; }

  .features { position: absolute; top: 587px; left: 0; width: 1200px; height: 325px; background: var(--panel); }
  .feature { position: absolute; text-align: center; background: var(--white); box-shadow: 0 1px 2px rgba(0,0,0,0.06); }
  .feature h3 { font-size: 11.5px; font-weight: 500; margin-top: 36px; letter-spacing: 0.2px; }
  .feature svg { display: block; margin: 14px auto 10px; }
  .feature p { font-size: 8.6px; line-height: 15px; color: var(--muted); padding: 0 20px; }
  .feature-skills { left: 234px; top: 75px; width: 232px; height: 175px; }
  .feature-calendar { left: 466px; top: 57px; width: 268px; height: 212px; background: var(--green); color: var(--white); z-index: 1; box-shadow: 0 2px 4px rgba(0,0,0,0.1); }
  .feature-calendar h3 { margin-top: 54px; }
  .feature-calendar p { color: var(--white); padding: 0 30px; }
  .feature-location { left: 734px; top: 75px; width: 231px; height: 175px; }

  .welcome { position: absolute; top: 912px; left: 0; width: 1200px; height: 288px; }
  .welcome h2 { position: absolute; left: 234px; top: 72px; font-size: 16px; font-weight: 500; letter-spacing: 0.2px; }
  .welcome .rule { position: absolute; left: 234px; top: 100px; width: 31px; height: 2px; background: var(--green); }
  .welcome p { position: absolute; left: 234px; top: 116px; width: 300px; font-size: 10px; line-height: 17.6px; color: var(--muted); }
  .welcome .frame { position: absolute; left: 619px; top: 69px; width: 353px; height: 187px; background: var(--green); }
  .welcome .photo { position: absolute; left: 613px; top: 75px; width: 352px; height: 188px;
    background: linear-gradient(120deg, #cfe3f2 0%, #a8c6de 45%, #b9c94a 75%, #8f9d3c 100%); }
</style>
</head>
<body>
  <header class="site-header">
    <div class="brand"><span class="brand-dot"></span>quarrynest</div>
    <nav class="main-nav">
      <a href="#" style="left:234px">HOME</a>
      <a href="#" style="left:303px">HOW IT WORKS</a>
      <a href="#" style="left:416px">ABOUT US</a>
      <a href="#" style="left:506px">OUR PARTNERS</a>
      <a href="#" style="left:620px">FAQ</a>
      <a href="#" style="left:678px">BLOG</a>
    </nav>
    <div class="btn-login">LOG IN</div>
    <div class="btn-register">REGISTER</div>
  </header>

  <section class="hero" role="img" aria-label="Smiling contractor in a white hard hat in front of a blurred construction team">
    <h1 class="hero-title"><span class="g">Available,</span> <span class="o">Quality Talent</span><br><span class="r">on Demand</span></h1>
    <p class="hero-copy">Quarrynest helps professional contractors to maximise their earning potential whilst enabling organisations to connect &amp; directly hire contingent talent in a much more efficient way than they do today.</p>
    <div class="join-outline"></div>
    <div class="btn-join">JOIN NOW ( Free )</div>
  </section>

  <section class="features">
    <article class="feature feature-skills">
      <h3>SKILLS MATCH</h3>
      <svg width="16" height="14" viewBox="0 0 16 14" fill="none" stroke="#9aa0a6" stroke-width="1"><path d="M4 1h8l3 4-7 8-7-8z M1 5h14 M6 1 5 5l3 8 3-8-1-4"/></svg>
      <p>Quarrynest has a secret sauce to find the right people to match the job requirements, put your roles, skills and experienced industry and we will do the rest to find the perfect match.</p>
    </article>
    <article class="feature feature-calendar">
      <h3>CALENDAR</h3>
      <svg width="15" height="16" viewBox="0 0 15 16" fill="none" stroke="#ffffff" stroke-width="1.4"><rect x="1" y="3" width="13" height="12"/><path d="M1 6.5h13 M4 1v4 M11 1v4"/></svg>
      <p>Uniquely Quarrynest has the visibility of contractors availability to work on projects, this is an active database that can predict talent pools ready-to-work at any one-time.</p>
    </article>
    <article class="feature feature-location">
      <h3>LOCATION</h3>
      <svg width="11" height="15" viewBox="0 0 11 15"><path d="M5.5 0C2.5 0 0 2.4 0 5.4 0 9.5 5.5 15 5.5 15S11 9.5 11 5.4C11 2.4 8.5 0 5.5 0z" fill="#b5b9bd"/><circle cx="5.5" cy="5.4" r="2" fill="#ffffff"/></svg>
      <p>Coupled with the skills &amp; availability the locations map you to the resources closest to the job, so you can confidently build a team of onsite local contractors across the nation.</p>
    </article>
  </section>

  <section class="welcome">
    <h2>WELCOME TO QUARRYNEST</h2>
    <div class="rule"></div>
    <p>Quarrynest is a unique marketplace providing contractors and companies a platform to connect in real-time by exposing the "availability status". Through intuitive search Quarrynest will instantly shortlist available contractors with matching skill criteria. This is an invaluable tool for companies finding the right people at the right time and at low cost!!</p>
    <div class="frame"></div>
    <div class="photo" role="img" aria-label="Two engineers in hard hats and high-visibility vests reviewing plans on site"></div>
  </section>
</body>
</html>
```